Seaside commercial building needs a design for a prominent sign

we have bought a small commercial building in a small seaside area. The building was in disrepair and we are rebuilding it and will rent to small businesses. We have a tall sign right on the corner of the area and want to design something special for the sign The address is 2738 and we want to incorporate that into the name, or just have that as the name. The area is called Bonnet Shores which we were going to use and call it Tidewell Corner. Almost all shops, however use Bonnet in their name. Looking for something unique with a sea-related logo. Elegant, yet welcoming.

```html
<!DOCTYPE html>
<html lang="en">
<head>
<meta charset="utf-8">
<title>Tidewell Corner – Corner Sign</title>
<link rel="stylesheet" href="https://fonts.googleapis.com/css2?family=Bebas+Neue&family=Kaushan+Script&family=Lobster&display=swap">
<style>
  :root {
    --backdrop: #ecebef;
    --sign-grey: #535456;
    --ornament-grey: #6a6b6e;
    --lettering: #ffffff;
    --band: #e6e3e8;
  }
  html, body {
    margin: 0;
    padding: 0;
    overflow: hidden;
  }
  .canvas {
    position: relative;
    width: 1200px;
    height: 750px;
    background: var(--backdrop);
    overflow: hidden;
  }
  .corner-sign {
    position: absolute;
    left: 390px;
    top: 30px;
    width: 400px;
    height: 690px;
  }
  .sign-frame { fill: var(--sign-grey); }
  .tenant-band { fill: var(--band); }
  .ornament-area { fill: var(--ornament-grey); }
  .address-oval {
    fill: none;
    stroke: var(--lettering);
    stroke-width: 2.5;
  }
  .sign-title {
    font-family: "Lobster", cursive;
    font-size: 40px;
    fill: var(--lettering);
  }
  .address-number {
    font-family: "Bebas Neue", sans-serif;
    font-size: 56px;
    fill: var(--lettering);
  }
  .tenant-name {
    font-family: "Kaushan Script", cursive;
    font-size: 38px;
    fill: var(--lettering);
  }
  .lease-notice {
    font-family: "Bebas Neue", sans-serif;
    font-size: 52px;
    letter-spacing: 1px;
    fill: var(--lettering);
  }
</style>
</head>
<body>
  <main class="canvas">
    <svg class="corner-sign" viewBox="0 0 400 690" xmlns="http://www.w3.org/2000/svg" aria-labelledby="sign-name">
      <title id="sign-name">Tidewell Corner 2738 tenant sign</title>
      <defs>
        <path id="title-arc" d="M 40 100 Q 198 50 360 100"/>
      </defs>

      <!-- posts and finials -->
      <rect class="sign-frame" x="11" y="19" width="12" height="50"/>
      <rect class="sign-frame" x="372" y="19" width="12" height="50"/>
      <circle class="sign-frame" cx="17" cy="22" r="17"/>
      <circle class="sign-frame" cx="378" cy="22" r="17"/>

      <!-- arched sign panel -->
      <path class="sign-frame" d="M 11 62 Q 198 -6 384 62 L 384 677 L 11 677 Z"/>

      <!-- name -->
      <text class="sign-title" text-anchor="middle">
        <textPath href="#title-arc" startOffset="50%">Tidewell Corner</textPath>
      </text>

      <!-- address -->
      <ellipse class="address-oval" cx="198" cy="137" rx="70" ry="39"/>
      <text class="address-number" x="198" y="157" text-anchor="middle">2738</text>

      <!-- sea ornament -->
      <rect class="ornament-area" x="8" y="188" width="380" height="52" rx="4"
            role="img" aria-label="Row of rolling wave scrolls in white line work"/>

      <!-- tenant bands -->
      <rect class="tenant-band" x="22" y="248" width="348" height="15"/>
      <rect class="tenant-band" x="22" y="339" width="348" height="16"/>
      <rect class="tenant-band" x="22" y="432" width="348" height="16"/>
      <rect class="tenant-band" x="22" y="525" width="348" height="17"/>
      <rect class="tenant-band" x="22" y="618" width="348" height="17"/>

      <!-- tenants -->
      <text class="tenant-name" x="196" y="312" text-anchor="middle">Marisol's Bakery</text>
      <text class="tenant-name" x="196" y="404" text-anchor="middle">Harlow Properties</text>
      <text class="lease-notice" x="196" y="503" text-anchor="middle">FOR LEASE</text>
    </svg>
  </main>
</body>
</html>
```